Build a landing page to promote a service (dialler consultation and support).

We are a call centre consultation firm and we need a landing page to promote a service. The service is Morvexa dialler consultation and support.
If you do not know what Morvexa is, please do some quick "Zumbrel" research for more information.
The landing page will be promoted with a paid advertisement, so we want something that is simple, and explains exactly what service we offer.
There are two objectives for the landing page:
1) A "call to action" which directs the user to a contact page, including a form plus all of our contact details.
2) A form for them viewers to enter their details to get a "FREE" quote for their project. This form should be placed on the main page.
Notes:
The call to action will require the viewer to enter their name, email, phone number as well as a description of their request. There will also need to be a drop down menu for the type of quote. This menu should have the following options:
1) Morvexa support
2) Morvexa hosting
3) Morvexa customisation
4) Other
We need 2 pages in total:
1) Main landing page
This is the home page. It will need to clearly indicate our services and our key selling features.
Services:
* Morvexa support
* Morvexa hosting
* Morvexa customisation
Key Selling Features:
* Australian based
* PCI complaint
* 10+ years of dialler and call centre experience
* we run a sister company which is a highly reputable 40 seat call centre, so we know first hand about call centre technology.
The main landing page will have an "about us" section with a few paragraphs about how we got started.
-------------------------------------------------------------------------
2) Contact page
All of our contact details will live on this page, as well as a contact form.
Other notes:
We will be self hosting the landing page.
We already have a domain name.
The design must be clean and incorporate our logo, as well as it's colours. (Logo attached)
We want a fully function HTML landing page, not just a "PSD" design.
The page must be mobile optimised.
Anyone using Morvexa software.

```html
<!DOCTYPE html>
<html lang="en">
<head>
<meta charset="utf-8">
<title>Dialwise – Morvexa support and call centre technology</title>
<link href="https://fonts.googleapis.com/css2?family=Lato:wght@400;700;900&display=swap" rel="stylesheet">
<style>
:root{
  --stage:#4d6c9f;
  --navy:#1e3553;
  --ink:#243552;
  --muted:#6b7a90;
  --accent:#d9775a;
  --pale:#e6eef8;
  --white:#ffffff;
  --icon:#6e91cf;
  --ring:#8fd0b2;
  --line:#c9d3e0;
}
*{box-sizing:border-box;margin:0;padding:0}
html,body{width:1200px;height:900px;overflow:hidden}
body{background:var(--stage);font-family:'Lato',sans-serif;color:var(--ink)}
.stage{display:flex;gap:36px;padding:24px 36px;height:900px}
.page{width:546px;background:var(--white);box-shadow:0 10px 30px rgba(0,0,0,.25);overflow:hidden;display:flex;flex-direction:column}
/* header */
.site-header{display:flex;align-items:center;justify-content:space-between;padding:0 22px;height:42px;background:var(--white)}
.brand{display:flex;align-items:center;gap:6px;font-size:15px;font-weight:700;color:var(--icon)}
.brand-dot{width:12px;height:12px;border-radius:50%;background:var(--icon)}
.nav{display:flex;align-items:center;gap:16px;font-size:7px;letter-spacing:.8px;text-transform:uppercase;color:var(--ink)}
.btn{display:inline-block;background:var(--accent);color:var(--white);font-weight:700;text-transform:uppercase;letter-spacing:.6px;border-radius:20px;font-size:8px;padding:6px 14px}
.nav .btn{font-size:6.5px;padding:5px 11px}
/* hero */
.hero{position:relative;height:262px;background:linear-gradient(100deg,#3e5f93 0%,#4f72a8 55%,#6f8fbf 100%);color:var(--white);padding:64px 26px 0}
.hero-copy{position:relative;max-width:300px}
.hero h1{font-size:25px;font-weight:700;line-height:1.15}
.hero p{font-size:9px;margin:10px 0 16px;line-height:1.5}
/* sections */
.section{background:var(--pale);padding:22px 24px;text-align:center}
.section.white{background:var(--white)}
.section h2{font-size:17px;font-weight:700;color:var(--ink);margin-bottom:16px}
.services{display:flex;justify-content:space-between;gap:14px}
.service{flex:1}
.service-icon{width:54px;height:54px;border-radius:50%;background:var(--icon);border:3px solid var(--ring);margin:0 auto 8px;display:flex;align-items:center;justify-content:center}
.service h3{font-size:9px;font-weight:700;margin-bottom:5px}
.service p,.feature p,.about p{font-size:7.5px;line-height:1.55;color:var(--muted)}
.section .btn{margin-top:14px}
.about p{max-width:420px;margin:0 auto 6px}
/* why */
.features{display:grid;grid-template-columns:1fr 1fr;gap:12px}
.feature{background:var(--white);padding:16px 14px;text-align:center}
.feature h3{font-size:8.5px;font-weight:700;margin:8px 0 5px}
.feature-art{height:36px;margin:0 auto;display:flex;align-items:center;justify-content:center}
.map-fill{width:52px;height:36px;border-radius:40% 45% 50% 35%;background:var(--icon)}
.badge{width:50px;height:30px;background:var(--icon);transform:skewX(-12deg)}
/* form */
.quote h2{margin-bottom:14px}
.form{display:grid;grid-template-columns:1fr 1fr;gap:8px 16px;text-align:left}
.field label{display:block;font-size:7px;margin-bottom:3px}
.field label span{color:var(--accent)}
.field .box{height:20px;border:1px solid var(--line);background:var(--white);font-size:7px;padding:5px 6px}
.field.wide{grid-column:1/3}
.field.wide .box{height:48px}
.quote .submit{text-align:center;margin-top:12px}
/* footer */
.site-footer{background:var(--navy);color:#c8d3e3;padding:18px 26px;display:flex;justify-content:space-between;font-size:7.5px;line-height:1.7;flex:1}
.site-footer h4{font-size:7.5px;font-weight:700;color:var(--white)}
.site-footer ul{list-style:none;text-transform:uppercase;letter-spacing:.6px;font-size:6.5px}
.site-footer .btn{margin-top:8px;font-size:6.5px}
.copyright{margin-top:8px;font-size:6.5px}
</style>
</head>
<body>
<main class="stage">
  <section class="page home-top">
    <header class="site-header">
      <div class="brand"><span class="brand-dot"></span>Dialwise</div>
      <nav class="nav"><span>Services</span><span>About us</span><span>Why Dialwise</span><span>Contact us</span><span class="btn">Get a quote</span></nav>
    </header>
    <div class="hero" role="img" aria-label="Call centre agents wearing headsets working at their computers, tinted blue">
      <div class="hero-copy">
        <h1>A holistic approach to Morvexa support and call centre technology</h1>
        <p>A complete Morvexa call center consultation for better service, productivity and profitability.</p>
        <span class="btn">Get a free quote</span>
      </div>
    </div>
    <div class="section services-section">
      <h2>Our Services</h2>
      <div class="services">
        <div class="service">
          <div class="service-icon"><svg width="24" height="24" viewBox="0 0 24 24" fill="none" stroke="#fff" stroke-width="1.6"><path d="M5 4h4l2 5-2.5 1.5a11 11 0 0 0 5 5L15 13l5 2v4a2 2 0 0 1-2 2A16 16 0 0 1 3 6a2 2 0 0 1 2-2z"/></svg></div>
          <h3>Morvexa support</h3>
          <p>We are dedicated to providing complete Morvexa support, including firewall, networking installation, problem tracing and fixing.</p>
        </div>
        <div class="service">
          <div class="service-icon"><svg width="22" height="22" viewBox="0 0 24 24" fill="none" stroke="#fff" stroke-width="1.6"><ellipse cx="12" cy="5" rx="8" ry="3"/><path d="M4 5v14c0 1.7 3.6 3 8 3s8-1.3 8-3V5M4 12c0 1.7 3.6 3 8 3s8-1.3 8-3"/></svg></div>
          <h3>Morvexa hosting</h3>
          <p>Dialwise ensures reliability, flawless service and high productivity with our Morvexa hosting facilities.</p>
        </div>
        <div class="service">
          <div class="service-icon"><svg width="22" height="22" viewBox="0 0 24 24" fill="none" stroke="#fff" stroke-width="1.6"><circle cx="12" cy="12" r="3"/><path d="M12 2v3M12 19v3M2 12h3M19 12h3M4.9 4.9l2.1 2.1M17 17l2.1 2.1M4.9 19.1L7 17M17 7l2.1-2.1"/></svg></div>
          <h3>Morvexa customisation</h3>
          <p>We customize your Morvexa as per your business requirements to ensure it fully meets your needs.</p>
        </div>
      </div>
      <span class="btn">Get a free quote</span>
    </div>
    <div class="section white about">
      <h2>About us</h2>
      <p>The story of Dialwise started when Sam Arlow, with a background of working in call centers, and Lee Varden with a history in technology, decided to team up and bring their skills to life.</p>
      <p>Sam started Brightside Contacts in 2014 and it has since grown to become a highly successful outbound call centre. Their combined knowledge let them build a technology framework from the ground up which has proven to be highly effective.</p>
    </div>
  </section>

  <section class="page home-bottom">
    <div class="section why">
      <h2>Why Dialwise</h2>
      <div class="features">
        <div class="feature">
          <div class="feature-art"><div class="map-fill" role="img" aria-label="Map of Australia"></div></div>
          <h3>Australian based company</h3>
          <p>We are a 100% Australian based and operated company, making it possible for us to continue placing a lot of importance on our customer service and providing you with the best customer support.</p>
        </div>
        <div class="feature">
          <div class="feature-art"><div class="badge" role="img" aria-label="Compliance certification badge"></div></div>
          <h3>PCI Compliant</h3>
          <p>We take safety and protection very seriously. This is why we are a fully PCI compliant company, making sure that we handle your data securely and as per the safety regulation.</p>
        </div>
        <div class="feature">
          <div class="feature-art"><div class="service-icon" style="width:36px;height:36px;margin:0"><svg width="18" height="18" viewBox="0 0 24 24" fill="none" stroke="#fff" stroke-width="1.8"><path d="M4 14v-2a8 8 0 0 1 16 0v2"/><rect x="3" y="13" width="4" height="6" rx="1"/><rect x="17" y="13" width="4" height="6" rx="1"/></svg></div></div>
          <h3>Dialler and Call Center Specialists</h3>
          <p>In addition to our long experience working in the dialler and call center industry, we also run a highly reputable 40 seat call centre. We know first hand about call centre technology and are specialists in the business.</p>
        </div>
        <div class="feature">
          <div class="feature-art"><div class="service-icon" style="width:36px;height:36px;margin:0;font-weight:900;color:#fff;font-size:14px">10</div></div>
          <h3>More than 10 years of experience</h3>
          <p>We have a 10+ years of dialler and call centre experience and understand the industry inside out. Because of that, our workforce is exceptionally skilled and offers a wide range of consulting and support solutions.</p>
        </div>
      </div>
    </div>
    <div class="section white quote">
      <h2>Get a free quote</h2>
      <form class="form">
        <div class="field"><label>Name <span>*</span></label><div class="box"></div></div>
        <div class="field"><label>Email <span>*</span></label><div class="box"></div></div>
        <div class="field"><label>Phone Number <span>*</span></label><div class="box"></div></div>
        <div class="field"><label>Dropdown <span>*</span></label><div class="box">Morvexa Support ▾</div></div>
        <div class="field wide"><label>Comment or Message <span>*</span></label><div class="box"></div></div>
      </form>
      <div class="submit"><span class="btn">Submit</span></div>
    </div>
    <footer class="site-footer">
      <div>
        <h4>Address</h4>
        <p>14/8 Carrow Street<br>Lindale, QLD 4600</p>
        <h4>Hours</h4>
        <p>Monday – Friday 9:00AM – 5:00PM</p>
        <span class="btn">Get a quote</span>
        <p class="copyright">Copyright © Dialwise</p>
      </div>
      <ul>
        <li>Services</li><li>About us</li><li>Why Dialwise</li><li>Contact us</li>
      </ul>
    </footer>
  </section>
</main>
</body>
</html>
```